Redesign Colorful Business Card

Please redesign the card attached. It is too busy. Please don't eliminate any of the words. The repetivite word "free" can be used less often.

Target Market(s)

College Students.

Contact Information for Business Card

The details listed in the attached image

Font styles to use
Sans Serif

Requirements
Must have
• A clear and simple presentation and must be attractive.

```html
<!DOCTYPE html>
<html lang="en">
<head>
<meta charset="utf-8">
<title>StudyNimbl Card</title>
<link rel="stylesheet" href="https://fonts.googleapis.com/css2?family=Montserrat:wght@800&family=Tinos&display=swap">
<style>
  :root {
    --navy: #23206f;
    --pink: #ff42d2;
    --blue: #0a6fbd;
    --green: #3a9a02;
    --white: #ffffff;
    --lilac: #8f7cf4;
    --lilac-deep: #6a52d8;
  }
  * { margin: 0; padding: 0; box-sizing: border-box; }
  html, body { width: 1200px; height: 780px; overflow: hidden; background: var(--navy); }
  .card {
    position: relative;
    width: 1200px;
    height: 780px;
    background: var(--navy);
    overflow: hidden;
    font-family: "Tinos", serif;
    color: var(--white);
  }
  .corner-cloud { position: absolute; left: 0; top: 0; }
  .site-name {
    position: absolute;
    left: 0; right: 0; top: 38px;
    text-align: center;
    font-family: "Montserrat", sans-serif;
    font-weight: 800;
    font-size: 72px;
    letter-spacing: 1px;
    line-height: 1;
  }
  .mascot-art {
    position: absolute;
    left: 20px; top: 140px;
    width: 640px; height: 520px;
    border-radius: 48% 52% 40% 44%;
    background: radial-gradient(ellipse at 45% 55%, var(--lilac) 0%, var(--lilac-deep) 60%, rgba(35,32,111,0) 75%);
  }
  .benefit {
    position: absolute;
    left: 693px;
    width: 412px;
    height: 182px;
    border-radius: 60px 110px 0 60px;
    text-transform: uppercase;
    display: flex;
    flex-direction: column;
    justify-content: center;
  }
  .benefit--time { top: 149px; background: var(--pink); padding-left: 16px; }
  .benefit--time .line-1 { font-size: 39px; line-height: 1.15; }
  .benefit--time .line-2 { font-size: 31px; line-height: 1.25; padding-left: 44px; }
  .benefit--class { top: 347px; background: var(--blue); padding-left: 42px; font-size: 29px; line-height: 1.22; }
  .benefit--memory { top: 545px; background: var(--green); padding-left: 104px; font-size: 37px; line-height: 1.2; }
  .copyright {
    position: absolute;
    left: 18px; top: 742px;
    font-size: 21px;
  }
</style>
</head>
<body>
<main class="card">
  <svg class="corner-cloud" width="380" height="190" viewBox="0 0 380 190" aria-hidden="true">
    <g fill="#ff42d2">
      <circle cx="40" cy="20" r="160"/>
      <circle cx="240" cy="-20" r="110"/>
      <circle cx="120" cy="60" r="70"/>
    </g>
  </svg>

  <h1 class="site-name">STUDYNIMBL.COM</h1>

  <div class="mascot-art" role="img" aria-label="Colourful cartoon elephant mascot spraying playful paint drops from its trunk"></div>

  <div class="benefit benefit--time">
    <span class="line-1">Cut study time</span>
    <span class="line-2">down by up to 50%</span>
  </div>
  <div class="benefit benefit--class">
    <span>Learn a subject<br>without having to<br>go to class</span>
  </div>
  <div class="benefit benefit--memory">
    <span>Memorize<br>anything<br>quickly</span>
  </div>

  <p class="copyright">Copyright Nimbl Services, LLC 2013-2022 All Rights Reserved</p>
</main>
</body>
</html>
```